Artist needs a business card for her pencil portraits and streetscapes

My mum is an artist and does fabulous portraits and sketches with pencil and needs a business card.
She likes designs that are a bit weird or unusual. The winning design will NOT be a slick modern corporate looking logo. It should be a little bit rustic and different. Interesting patterns and textures would be great, it doesn't even need to look like a business card! Come up with something unique!

Target Market(s)

Older clientele looking for family portraits

Industry/Entity Type

Artists

Contact Information for Business Card

Basically just need the name and contact details

Font styles to use
Decorative
Script

Requirements
Must have
• Lena Brodsworth
• Artist
• 0427913562
• lenabrodsworth@quillpost.example
Nice to have
• Weird artistic backgrounds, interesting textures, unusual designs for an artistic woman.
Should not have
• Nothing ultra modern and nothing corporate looking.

```html
<!DOCTYPE html>
<html lang="en">
<head>
<meta charset="utf-8">
<title>Lena Brodsworth — Artist — Business Card</title>
<link rel="stylesheet" href="https://fonts.googleapis.com/css2?family=Allura&display=swap">
<style>
  :root {
    --page-bg: #d9d9d7;
    --card-cream: #f6efe0;
    --card-butter: #efe7c9;
    --card-blush: #eedccd;
    --card-sage: #cfd6c8;
    --card-blue: #9fb3c4;
    --card-slate: #8ea3b8;
    --ink: #1d1b1c;
    --script: "Allura", cursive;
  }
  * { box-sizing: border-box; margin: 0; padding: 0; }
  html, body {
    width: 1200px;
    height: 1200px;
    overflow: hidden;
    background: var(--page-bg);
  }
  .canvas {
    position: relative;
    width: 1200px;
    height: 1200px;
    display: flex;
    align-items: center;
    justify-content: center;
  }
  .business-card {
    position: relative;
    width: 1000px;
    height: 572px;
    overflow: hidden;
    box-shadow: 0 6px 18px rgba(0,0,0,0.18);
    background: var(--card-cream);
  }
  .watercolour-wash {
    position: absolute;
    inset: 0;
    width: 100%;
    height: 100%;
  }
  .card-text {
    position: absolute;
    inset: 0;
    font-family: var(--script);
    color: var(--ink);
  }
  .artist-name {
    position: absolute;
    left: 0;
    right: 0;
    top: 70px;
    text-align: center;
    font-size: 96px;
    font-weight: 400;
    line-height: 1;
  }
  .artist-role {
    position: absolute;
    left: 390px;
    top: 168px;
    font-size: 66px;
    line-height: 1;
  }
  .contact-phone {
    position: absolute;
    left: 0;
    right: 0;
    top: 292px;
    text-align: center;
    font-size: 60px;
    line-height: 1;
    letter-spacing: 1px;
  }
  .contact-email {
    position: absolute;
    left: 0;
    right: 0;
    top: 368px;
    text-align: center;
    font-size: 64px;
    line-height: 1;
  }
</style>
</head>
<body>
<main class="canvas">
  <section class="business-card">
    <svg class="watercolour-wash" viewBox="0 0 1000 572" preserveAspectRatio="none"
         role="img" aria-label="Soft watercolour wash in cream, blush and dusty blue tones">
      <defs>
        <linearGradient id="wash-base" x1="0" y1="0" x2="0.35" y2="1">
          <stop offset="0" stop-color="var(--card-cream)"/>
          <stop offset="0.35" stop-color="var(--card-blush)"/>
          <stop offset="0.6" stop-color="var(--card-butter)"/>
          <stop offset="0.8" stop-color="var(--card-sage)"/>
          <stop offset="1" stop-color="var(--card-blue)"/>
        </linearGradient>
        <radialGradient id="wash-corner" cx="1" cy="0.75" r="0.6">
          <stop offset="0" stop-color="var(--card-slate)" stop-opacity="0.85"/>
          <stop offset="1" stop-color="var(--card-slate)" stop-opacity="0"/>
        </radialGradient>
      </defs>
      <rect width="1000" height="572" fill="url(#wash-base)"/>
      <rect width="1000" height="572" fill="url(#wash-corner)"/>
    </svg>
    <div class="card-text">
      <h1 class="artist-name">Lena Brodsworth</h1>
      <p class="artist-role">- Artist</p>
      <p class="contact-phone">0427913562</p>
      <p class="contact-email">lenabrodsworth@quillpost.example</p>
    </div>
  </section>
</main>
</body>
</html>
```